Supplier Hub Landing Page with Dynamic Widgets

We represent Automotive Parts Suppliers across Canada, the US and UK our website is kelvoro.com. We are looking to provide our clients with a Supplier Hub where they can login and see multiple graphical widgets that will load account and sales and marketing information based on our internal database queries. The design should mirror our corporate website and the widgets should be professional with graph elements. The page needs to handle varying number of dynamic widgets as these change depending on the database. We have included a simple wire frame landing page with a few other slides to get the idea across but please use your design skills to create something that will wow our clients. These widgets will open additional pages when clicked on so please include a few linked page designs as well i.e. Accounts - show invoicing, Agreements - shows all current and past agreements, Action Alerts - show all actions we sent them from our field reps... etc. Our developers will take care of the coding so we just need some amazing design - simple is always better. These will also need to be responsive for mobile.

Target Market(s)

Automotive Parts Suppliers, OE Vehicle Manufacturers, Automotive Insurers

Industry/Entity Type

Automotive

Number of Pages Required

5+ page

Font styles to use
Sans Serif

Colors

Designer to choose colors to be used in the design.

Requirements
Must have
• Professional corporate design. Landing page with dynamic widgets and graphs and a few page designs the widget link to. Design must mirror our corporate website
Should not have
• No illustrations or cartoon type images.

```html
<!DOCTYPE html>
<html lang="en">
<head>
<meta charset="utf-8">
<title>Supplier Hub – Kelvoro Parts Solutions</title>
<link rel="stylesheet" href="https://fonts.googleapis.com/css2?family=Roboto+Condensed:wght@400;700&family=Roboto:wght@400;500;700&display=swap">
<style>
:root{
  --red:#d0112b;
  --green:#12c912;
  --side:#262626;
  --page:#f3f3f3;
  --card:#ffffff;
  --ink:#262626;
  --muted:#444;
  --grey:#d0d0d0;
}
*{box-sizing:border-box;margin:0;padding:0}
html,body{width:1200px;height:785px;overflow:hidden;background:var(--page);font-family:"Roboto",sans-serif;color:var(--ink)}
.hub{position:relative;width:1200px;height:785px}
.abs{position:absolute}
.cond{font-family:"Roboto Condensed",sans-serif;font-weight:700}

/* sidebar */
.sidebar{left:0;top:0;width:169px;height:785px;background:var(--side);color:#fff}
.brand{position:absolute;left:20px;top:25px;display:flex;align-items:center;gap:7px}
.brand-dot{width:31px;height:31px;border-radius:50%;background:var(--red)}
.brand-name{font-family:"Roboto Condensed",sans-serif;font-weight:700;font-size:13px;letter-spacing:.5px;line-height:1}
.nav-item{position:absolute;left:0;width:169px;height:44px;display:flex;align-items:center;padding-left:20px;gap:14px;font-family:"Roboto Condensed",sans-serif;font-weight:700;font-size:10.5px}
.nav-item svg{width:19px;height:19px;fill:#fff;flex:none}
.nav-item.active{background:var(--red)}

/* top bar */
.search{left:220px;top:18px;width:345px;height:29px;background:#f7f7f7;border:1px solid #ddd;display:flex;align-items:center;justify-content:space-between;padding:0 18px 0 25px;font-size:9px;color:#333}
.avatar{left:1015px;top:18px;width:32px;height:32px;border-radius:50%;background:linear-gradient(#6b5a4e,#3a3430)}
.greet{left:1059px;top:27px;font-size:12px}

.title{left:221px;top:95px;font-size:27px;color:#222}

.stat{top:88px;height:50px;background:var(--card);box-shadow:0 2px 6px rgba(0,0,0,.05);text-align:center;font-family:"Roboto Condensed",sans-serif;font-weight:700;font-size:12px;line-height:1.45;padding-top:9px}
.stat b{display:block;font-size:15px;line-height:1.1}

.card{background:var(--card);box-shadow:0 3px 10px rgba(0,0,0,.06);text-align:center}
.card h2{font-family:"Roboto Condensed",sans-serif;font-weight:700;font-size:16px;line-height:1.2;color:#222}
.gear{position:absolute;right:12px;top:12px;width:11px;height:11px}
.small{font-size:9.5px;color:#333;line-height:1.15}
.num{font-family:"Roboto Condensed",sans-serif;font-weight:700;font-size:19px;color:var(--red);line-height:1.25}

.status{background:var(--green);color:#fff}
.status h2{color:#fff;margin-top:35px}
.status .tick{margin:20px auto 0;display:block}
.status .big{font-family:"Roboto Condensed",sans-serif;font-weight:700;font-size:24px;line-height:1.15;margin-top:22px}

.contact-line{display:flex;justify-content:center;align-items:center;gap:6px;font-size:9.5px;margin-top:9px}
.contact-line svg{width:12px;height:9px;fill:var(--red)}

.legend{display:flex;align-items:center;gap:8px;font-family:"Roboto Condensed",sans-serif;font-size:11.5px;font-weight:700;margin-left:43px;margin-top:8px}
.legend i{width:11px;height:11px;display:inline-block}
.legend span{margin-left:6px}

.footer{left:169px;top:722px;width:1031px;height:63px;background:#fff;text-align:center;font-size:8.5px;color:#444;padding-top:26px}
</style>
</head>
<body>
<div class="hub">

  <aside class="abs sidebar">
    <div class="brand"><span class="brand-dot"></span><span class="brand-name">KELVORO</span></div>

    <div class="nav-item active" style="top:99px"><svg viewBox="0 0 20 20"><rect x="0" y="0" width="8" height="11"/><rect x="10" y="0" width="10" height="6"/><rect x="10" y="8" width="10" height="12"/><rect x="0" y="13" width="8" height="7"/></svg>Dashboard Home</div>
    <div class="nav-item" style="top:143px"><svg viewBox="0 0 20 20"><path d="M10 1c-3.5 0-6 2.6-6 6.5v5L2 15v1h16v-1l-2-2.5v-5C16 3.6 13.5 1 10 1zM8 17.5a2 2 0 0 0 4 0z"/></svg>Notifications</div>
    <div class="nav-item" style="top:186px"><svg viewBox="0 0 20 20"><rect x="1" y="14" width="2.5" height="5"/><rect x="5" y="11" width="2.5" height="8"/><rect x="9" y="8" width="2.5" height="11"/><rect x="13" y="5" width="2.5" height="14"/><path d="M1 10l6-5 4 2 7-6" stroke="#fff" stroke-width="1.3" fill="none"/></svg>Sales and Marketing</div>
    <div class="nav-item" style="top:230px"><svg viewBox="0 0 20 20"><path d="M2 2h13v17H2z"/><path d="M4 6h9M4 9.5h9M4 13h9" stroke="#262626" stroke-width="1.4"/><rect x="16" y="3" width="2.5" height="14"/></svg>Your Orders</div>
    <div class="nav-item" style="top:274px"><svg viewBox="0 0 20 20"><circle cx="7" cy="3" r="2.5"/><path d="M5 6h4l1 5 3 2-1 1.5-4-2-1 3 2 4H7l-2-4 1-5-2 1-1 3H1.5l1.3-4.5z"/><rect x="12" y="15" width="7" height="4"/></svg>Find Supplier</div>
    <div class="nav-item" style="top:319px"><svg viewBox="0 0 20 20"><path d="M2 4h11v15H2z"/><path d="M4 8h7M4 11h7M4 14h7" stroke="#262626" stroke-width="1.3"/><circle cx="15.5" cy="4.5" r="3.5"/></svg>Invoices</div>
    <div class="nav-item" style="top:361px"><svg viewBox="0 0 20 20"><path d="M8.5 0h3l.5 2.6 2 .9 2.2-1.5 2.1 2.1-1.5 2.2.9 2 2.6.5v3l-2.6.5-.9 2 1.5 2.2-2.1 2.1-2.2-1.5-2 .9-.5 2.6h-3l-.5-2.6-2-.9-2.2 1.5-2.1-2.1 1.5-2.2-.9-2L0 11.5v-3l2.6-.5.9-2L2 3.8l2.1-2.1 2.2 1.5 2-.9zM10 6.5a3.5 3.5 0 1 0 0 7 3.5 3.5 0 0 0 0-7z"/></svg>Settings</div>
  </aside>

  <div class="abs search"><span>Search</span><svg width="13" height="13" viewBox="0 0 14 14"><circle cx="5.5" cy="5.5" r="4.3" fill="none" stroke="#111" stroke-width="1.6"/><path d="M8.7 8.7l4.3 4.3" stroke="#111" stroke-width="1.8"/></svg></div>
  <div class="abs avatar" role="img" aria-label="Profile photo of the signed-in user"></div>
  <div class="abs greet cond">Hi Reid Gears!</div>

  <h1 class="abs title cond">Supplier Hub</h1>

  <div class="abs stat" style="left:419px;width:172px">For the month of<b>JANUARY 2020</b></div>
  <div class="abs stat" style="left:614px;width:172px">Shop Visits<b>136</b></div>
  <div class="abs stat" style="left:809px;width:155px">Marketing Touches<b>323</b></div>
  <div class="abs stat" style="left:987px;width:156px">NPS Score<b>81</b></div>

  <!-- representative -->
  <section class="abs card" style="left:221px;top:160px;width:172px;height:287px">
    <svg class="gear" viewBox="0 0 20 20"><circle cx="10" cy="10" r="7" fill="none" stroke="#999" stroke-width="2" stroke-dasharray="3 2"/><circle cx="10" cy="10" r="3" fill="none" stroke="#999" stroke-width="1.5"/></svg>
    <h2 style="margin-top:36px">Your Kelvoro<br>Representative</h2>
    <div role="img" aria-label="Portrait of the account representative" style="width:50px;height:50px;border-radius:50%;margin:24px auto 0;background:linear-gradient(#d9b98c,#8a6a4e)"></div>
    <div class="cond" style="font-size:14px;margin-top:22px">Marla Voss</div>
    <div class="small" style="margin-top:8px">BDM Vancouver/ N. Shore</div>
    <div class="contact-line"><svg viewBox="0 0 12 9"><path d="M0 3C2-1 10-1 12 3L10 4 9 2.5H3L2 4zM3 4h6l2 5H1z"/></svg>Phone:-.604.555.0148</div>
    <div class="contact-line"><svg viewBox="0 0 12 9"><rect width="12" height="9"/><path d="M0 0l6 5 6-5" stroke="#fff" fill="none"/></svg>mvoss@kelvoro.com</div>
  </section>

  <!-- contact -->
  <section class="abs card" style="left:221px;top:469px;width:172px;height:148px">
    <svg class="gear" viewBox="0 0 20 20"><circle cx="10" cy="10" r="7" fill="none" stroke="#999" stroke-width="2" stroke-dasharray="3 2"/><circle cx="10" cy="10" r="3" fill="none" stroke="#999" stroke-width="1.5"/></svg>
    <h2 style="margin-top:36px">Contact Us</h2>
    <div class="contact-line" style="margin-top:14px"><svg viewBox="0 0 12 9"><path d="M0 3C2-1 10-1 12 3L10 4 9 2.5H3L2 4zM3 4h6l2 5H1z"/></svg>877.555.0190</div>
    <div class="contact-line"><svg viewBox="0 0 12 9"><rect width="12" height="9"/><path d="M0 0l6 5 6-5" stroke="#fff" fill="none"/></svg>info@kelvoro.com</div>
  </section>

  <!-- account status -->
  <section class="abs card status" style="left:416px;top:160px;width:172px;height:237px">
    <h2>Account Status</h2>
    <svg class="tick" width="53" height="53" viewBox="0 0 53 53"><circle cx="26.5" cy="26.5" r="26.5" fill="#fff"/><path d="M14 27l9 9 17-18" stroke="var(--green)" stroke-width="6" fill="none"/></svg>
    <div class="big">$0<br>Due</div>
  </section>

  <!-- agreements -->
  <section class="abs card status" style="left:611px;top:160px;width:172px;height:237px">
    <h2>Agreements</h2>
    <svg class="tick" width="53" height="53" viewBox="0 0 53 53"><circle cx="26.5" cy="26.5" r="26.5" fill="#fff"/><path d="M14 27l9 9 17-18" stroke="var(--green)" stroke-width="6" fill="none"/></svg>
    <div class="big">Agreement<br>Status</div>
  </section>

  <!-- early bird -->
  <section class="abs card" style="left:806px;top:160px;width:337px;height:237px;text-align:left">
    <h2 style="position:absolute;left:30px;top:34px">Early Bird Special!</h2>
    <p class="small" style="position:absolute;left:30px;top:76px;width:120px;line-height:1.6">Save 15% if you take Kelvoro of our Early Bird Promotion for your 2020 Calendars</p>
    <p class="cond" style="position:absolute;left:30px;top:172px;font-size:10px;line-height:1.55">Call your Kelvoro<br>BDM today!</p>
    <div role="img" aria-label="Sample 2020 wall calendar with a car photo and monthly grid" style="position:absolute;left:200px;top:40px;width:105px;height:156px;background:linear-gradient(#3a3f46 0 34%,#f4f4f4 34%);box-shadow:0 2px 6px rgba(0,0,0,.25);border:3px solid #fff"></div>
  </section>

  <!-- rewards -->
  <section class="abs card" style="left:416px;top:419px;width:172px;height:253px">
    <h2 style="margin-top:36px">Kelvoro<br>Rewards</h2>
    <div class="small" style="font-size:11px;margin-top:18px">Balance</div><div class="num">350</div>
    <div class="small" style="font-size:11px;margin-top:6px">Assigned</div><div class="num">400</div>
    <div class="small" style="font-size:11px;margin-top:6px">Purchased</div><div class="num">500</div>
  </section>

  <!-- marketing -->
  <section class="abs card" style="left:611px;top:419px;width:172px;height:253px">
    <h2 style="margin-top:36px">Marketing</h2>
    <svg width="56" height="56" viewBox="0 0 56 56" style="display:block;margin:20px auto 0">
      <circle cx="24" cy="32" r="21" fill="var(--red)"/><circle cx="24" cy="32" r="15" fill="#fff"/><circle cx="24" cy="32" r="10" fill="var(--red)"/><circle cx="24" cy="32" r="5" fill="#fff"/>
      <path d="M24 32L48 8" stroke="var(--red)" stroke-width="4"/><path d="M42 6l6-5 1 7 7 1-5 6-7-1z" fill="var(--red)"/>
    </svg>
    <div class="small" style="font-size:11px;margin-top:22px">Marketing<br>Touches</div>
    <div class="num">750</div>
  </section>

  <!-- repairer database -->
  <section class="abs card" style="left:806px;top:419px;width:155px;height:253px">
    <h2 style="margin-top:36px">Repairer Database</h2>
    <svg width="155" height="110" viewBox="0 0 155 110" style="display:block;margin-top:4px">
      <g transform="rotate(-90 77 63)">
        <circle cx="77" cy="63" r="31" fill="none" stroke="var(--grey)" stroke-width="18"/>
        <circle cx="77" cy="63" r="31" fill="none" stroke="var(--green)" stroke-width="18" stroke-dasharray="16 195"/>
        <circle cx="77" cy="63" r="31" fill="none" stroke="var(--red)" stroke-width="18" stroke-dasharray="0 16 63 195"/>
      </g>
      <g font-family="Roboto" font-size="6.5" fill="#222" text-anchor="middle">
        <text x="99" y="10">50</text><text x="99" y="18">A Rated</text>
        <text x="133" y="54">250</text><text x="133" y="62">B Rated</text>
        <text x="22" y="70">600</text><text x="22" y="78">C Rated</text>
      </g>
    </svg>
    <div class="num" style="margin-top:4px">1000</div>
    <div class="small">Total</div>
  </section>

  <!-- action alerts -->
  <section class="abs card" style="left:984px;top:419px;width:155px;height:253px;text-align:left">
    <h2 style="margin-top:36px;text-align:center">Action Alerts</h2>
    <svg width="82" height="82" viewBox="0 0 82 82" style="display:block;margin:18px auto 0">
      <g transform="rotate(-90 41 41)">
        <circle cx="41" cy="41" r="30" fill="none" stroke="var(--grey)" stroke-width="20"/>
        <circle cx="41" cy="41" r="30" fill="none" stroke="var(--green)" stroke-width="20" stroke-dasharray="23 189"/>
      </g>
    </svg>
    <div class="legend" style="margin-top:22px"><i style="background:var(--green)"></i>MTH<span>36</span></div>
    <div class="legend"><i style="background:var(--grey)"></i>YTD<span>267</span></div>
  </section>

  <footer class="abs footer">Copyright © 2020 Kelvoro Parts Solutions Ltd.</footer>
</div>
</body>
</html>
```